professional business card design

Business card design. Photos have been uploaded and i am open to the designer choosing which photos to use. Would like the card to be mostyly in a grey scale design with black, whites, silver & grey colours. I have added copy of our flyer as would like on the back side of card our services to be listed. Do not use any bright colurs such as blue red green or yellow. i need to be able to edit the phone number and naem in the final card design submitted.

Target Market(s)

Clients

Industry/Entity Type

earhmovibng and transport

Contact Information for Business Card

Director Name, address, email, phone number and services

Colors

Designer to choose only greyscale colors for use in the design.

Requirements
Should not have
• no yellow, red, blue or green

```html
<!DOCTYPE html>
<html lang="en">
<head>
<meta charset="utf-8">
<title>Ridgeway Haulage – Business Card</title>
<link href="https://fonts.googleapis.com/css2?family=Roboto:wght@300;400;500;700&display=swap" rel="stylesheet">
<style>
  :root {
    --page-bg: #e9e9e9;
    --card-black: #050505;
    --card-white: #ffffff;
    --ink: #111111;
    --text-light: #f2f2f2;
    --silver: #c9c9c9;
    --steel-mid: #4a4a4a;
    --steel-dark: #1c1c1c;
    --dust-light: #d9a878;
    --dust-deep: #b8743f;
    --card-shadow: 0 3px 8px rgba(0,0,0,0.28);
  }
  * { margin: 0; padding: 0; box-sizing: border-box; }
  html, body {
    width: 1106px; height: 1200px; overflow: hidden;
    background: var(--page-bg);
    font-family: "Roboto", Arial, sans-serif;
  }
  .card {
    position: absolute; left: 131px; width: 842px;
    overflow: hidden; box-shadow: var(--card-shadow);
  }
  /* Front */
  .card-front { top: 85px; height: 492px; background: var(--card-black); }
  .front-texture {
    position: absolute; left: 150px; top: 0; width: 560px; height: 330px;
    background: radial-gradient(ellipse at 50% 40%, #3a3a3a 0%, #1a1a1a 45%, rgba(5,5,5,0) 75%);
  }
  .brand {
    position: absolute; left: 0; right: 0; top: 58px; text-align: center;
    color: var(--silver); font-weight: 700; font-size: 64px; letter-spacing: 2px; line-height: 1;
  }
  .brand-sub {
    position: absolute; left: 0; right: 0; top: 150px; text-align: center;
    color: var(--silver); font-weight: 700; font-size: 22px; line-height: 1;
  }
  .fleet-photo {
    position: absolute; left: 23px; top: 253px; width: 801px; height: 180px;
    background: linear-gradient(180deg, #2c2c2c 0%, #5a5a5a 55%, #1a1a1a 85%, rgba(5,5,5,0) 100%);
    opacity: 0.85;
  }
  .holder-name {
    position: absolute; right: 511px; top: 365px;
    color: var(--text-light); font-weight: 500; font-size: 37px; line-height: 1;
  }
  .holder-title {
    position: absolute; right: 511px; top: 410px;
    color: var(--text-light); font-weight: 300; font-size: 21px; line-height: 1;
  }
  .contact-list { position: absolute; right: 48px; top: 312px; list-style: none; }
  .contact-list li {
    display: flex; justify-content: flex-end; align-items: center; gap: 14px;
    height: 32px; color: var(--text-light); font-weight: 300; font-size: 21px;
  }
  .contact-list svg { width: 13px; height: 13px; fill: var(--text-light); }

  /* Back */
  .card-back { top: 623px; height: 489px; background: var(--card-white); }
  .services-title {
    position: absolute; left: 58px; top: 70px;
    color: var(--ink); font-weight: 700; font-size: 44px; line-height: 1;
  }
  .truck-photo {
    position: absolute; left: 430px; top: 58px; width: 344px; height: 80px;
    background: linear-gradient(90deg, #1e1e1e 0%, #3b3b3b 40%, #2a2a2a 70%, #444 100%);
    border-radius: 4px;
  }
  .road-photo {
    position: absolute; left: 0; top: 300px; width: 842px; height: 189px;
    background: linear-gradient(180deg, rgba(255,255,255,1) 0%, #9a9a9a 25%, #3a3a3a 45%, var(--dust-light) 65%, var(--dust-deep) 100%);
  }
  .service-list {
    position: absolute; top: 175px; list-style: none;
    color: var(--ink); font-size: 21px; line-height: 27px;
  }
  .service-list.col-left { left: 58px; }
  .service-list.col-right { left: 495px; }
  .service-list li { padding-left: 12px; text-indent: -12px; }
  .service-list li::before { content: "•"; display: inline-block; width: 12px; text-indent: 0; }
</style>
</head>
<body>

<section class="card card-front">
  <div class="front-texture" role="img" aria-label="Dark perforated metal texture"></div>
  <div class="brand">RIDGEWAY</div>
  <div class="brand-sub">Haulage Pty Ltd</div>
  <div class="fleet-photo" role="img" aria-label="Greyscale photo of a road train with three tipper trailers on an outback road"></div>

  <div class="holder-name">DALE MORROW</div>
  <div class="holder-title">General Manager</div>

  <ul class="contact-list">
    <li>402-555-0147
      <svg viewBox="0 0 24 24" aria-hidden="true"><path d="M6.6 10.8a15 15 0 0 0 6.6 6.6l2.2-2.2c.3-.3.7-.4 1-.2 1.1.4 2.3.6 3.6.6.6 0 1 .4 1 1V20c0 .6-.4 1-1 1A17 17 0 0 1 3 4c0-.6.4-1 1-1h3.5c.6 0 1 .4 1 1 0 1.3.2 2.5.6 3.6.1.3 0 .7-.2 1z"/></svg>
    </li>
    <li>dmorrow@ridgeway.com
      <svg viewBox="0 0 24 24" aria-hidden="true"><path d="M2 5h20v14H2z M3 6l9 7 9-7" fill="none" stroke="#f2f2f2" stroke-width="2"/></svg>
    </li>
    <li>www.ridgeway.com
      <svg viewBox="0 0 24 24" aria-hidden="true"><circle cx="12" cy="12" r="10" fill="none" stroke="#f2f2f2" stroke-width="2"/><path d="M2 12h20M12 2c3 3 3 17 0 20M12 2c-3 3-3 17 0 20" fill="none" stroke="#f2f2f2" stroke-width="1.6"/></svg>
    </li>
    <li>18 Quarry Rd, Lenton RI 02010
      <svg viewBox="0 0 24 24" aria-hidden="true"><path d="M12 2a7 7 0 0 0-7 7c0 5 7 13 7 13s7-8 7-13a7 7 0 0 0-7-7zm0 9.5A2.5 2.5 0 1 1 12 6.5a2.5 2.5 0 0 1 0 5z"/></svg>
    </li>
  </ul>
</section>

<section class="card card-back">
  <div class="road-photo" role="img" aria-label="Photo of a road train on a red dirt outback road"></div>
  <h2 class="services-title">Our Services</h2>
  <div class="truck-photo" role="img" aria-label="Photo of a black road train with three trailers"></div>

  <ul class="service-list col-left">
    <li>Over size loades/Hot shots loads</li>
    <li>Heavy vehicle recovery services</li>
    <li>Portable Water Deliveries</li>
    <li>Road Buildings/Maintenance</li>
    <li>Earthworks</li>
    <li>Sand &amp; Metal Supply &amp; Cartage</li>
  </ul>
  <ul class="service-list col-right">
    <li>Road Train Tippers</li>
    <li>Road Train Tankers</li>
    <li>Road Train Flat Tops</li>
    <li>Drop Deck Trailers</li>
    <li>Mine Site accredited equipment &amp; Operators</li>
  </ul>
</section>

</body>
</html>
```